Stationery Design Project

We need a stationary design for a well-known architect in Guadalajara, Mexico. This architect specializes in very luxurious homes and commercial developments. His clients are very sophisticated, so the letterhead should be equally sophisticated. References to mythology, etc. might be a plus. The letterhead may be embossed and will be printed on a heavy-weight linen. His homes and developments are very luxurious but not necessarily ultra-modern in their aesthetic.
Target Market(s)
High end developers and luxury home buyers
Industry/Entity Type
Architect
Look and feel

```html
<!DOCTYPE html>
<html lang="en">
<head>
<meta charset="utf-8">
<title>Tomás Ibarrola Architect — Stationery</title>
<link href="https://fonts.googleapis.com/css2?family=Cinzel:wght@500&family=Arimo&family=Lato:wght@400&display=swap" rel="stylesheet">
<style>
  :root {
    --backdrop: #f3f2f0;
    --paper: #ffffff;
    --ink: #111111;
    --ink-soft: #444444;
    --rule: #9a9a9a;
    --brand-blue: #4f7fc2;
    --brand-blue-light: #6798d2;
    --shadow: 0 2px 8px rgba(0,0,0,0.18);
  }
  * { margin: 0; padding: 0; box-sizing: border-box; }
  html, body { width: 1200px; height: 914px; overflow: hidden; background: var(--backdrop); }
  .sheet { position: relative; width: 1200px; height: 914px; }

  .brand { position: absolute; text-align: center; font-family: 'Cinzel', serif; font-weight: 500; color: var(--ink); line-height: 1; }
  .brand-dot { display: block; margin: 0 auto; border-radius: 50%; background: var(--brand-blue); }
  .brand-name { display: block; white-space: nowrap; }
  .brand-role { display: block; white-space: nowrap; }

  /* Letterhead */
  .letterhead { position: absolute; left: 56px; top: 29px; width: 607px; height: 859px; background: var(--paper); box-shadow: var(--shadow); }
  .letterhead-frame { position: absolute; left: 42px; top: 90px; width: 523px; height: 714px; }
  .letterhead .brand { left: 0; width: 607px; top: 32px; }
  .letterhead .brand-dot { width: 52px; height: 52px; margin-bottom: 14px; }
  .letterhead .brand-name { font-size: 16px; }
  .letterhead .brand-role { font-size: 10px; letter-spacing: 3px; margin-top: 2px; }
  .letterhead-contact { position: absolute; left: 0; width: 607px; top: 765px; text-align: center; font-family: 'Arimo', Arial, sans-serif; font-size: 11.5px; line-height: 13.3px; color: var(--ink-soft); }
  .letterhead-contact .tel { margin-top: 13px; }

  /* Card labels */
  .card-label { position: absolute; left: 720px; font-family: 'Lato', Arial, sans-serif; font-size: 23px; color: var(--ink); letter-spacing: -0.3px; }

  /* Business card back */
  .card { position: absolute; left: 746px; width: 399px; height: 228px; box-shadow: var(--shadow); }
  .card-back { top: 85px; background: linear-gradient(180deg, var(--brand-blue), var(--brand-blue-light)); }
  .card-back .brand { left: 0; width: 399px; top: 38px; color: #ffffff; }
  .card-back .brand-dot { width: 96px; height: 96px; background: rgba(255,255,255,0.95); margin-bottom: 20px; }
  .card-back .brand-name { font-size: 26px; }
  .card-back .brand-role { font-size: 16px; letter-spacing: 5px; margin-top: 3px; }

  /* Business card front */
  .card-front { top: 354px; background: var(--paper); }
  .card-front .brand { left: 36px; width: 160px; top: 58px; }
  .card-front .brand-dot { width: 56px; height: 56px; margin-bottom: 14px; }
  .card-front .brand-name { font-size: 16px; }
  .card-front .brand-role { font-size: 10px; letter-spacing: 3px; margin-top: 2px; }
  .card-divider { position: absolute; left: 210px; top: 52px; width: 1px; height: 124px; background: var(--rule); }
  .card-contact { position: absolute; left: 222px; top: 82px; font-family: 'Lato', Arial, sans-serif; font-size: 10.5px; line-height: 12.8px; color: var(--ink-soft); }
  .card-contact .tel { margin-top: 12px; letter-spacing: 0.6px; }

  /* Primary logo lockup */
  .brand-primary { left: 742px; width: 400px; top: 606px; }
  .brand-primary .brand-dot { width: 160px; height: 160px; margin-bottom: 18px; }
  .brand-primary .brand-name { font-size: 34px; }
  .brand-primary .brand-role { font-size: 24px; letter-spacing: 7px; margin-top: 2px; }
</style>
</head>
<body>
<main class="sheet">

  <section class="letterhead" aria-label="Letterhead">
    <svg class="letterhead-frame" width="523" height="714" viewBox="0 0 523 714" aria-hidden="true">
      <path d="M176 0.5 H0.5 V713.5 H176 M346 713.5 H522.5 V0.5 H346" fill="none" stroke="var(--rule)" stroke-width="1"/>
    </svg>
    <div class="brand">
      <span class="brand-dot"></span>
      <span class="brand-name">Tomás Ibarrola</span>
      <span class="brand-role">Architect</span>
    </div>
    <address class="letterhead-contact" style="font-style:normal">
      <div>Arq. Tomás Ibarrola</div>
      <div>Calle de los Fresnos #1540</div>
      <div>Colinas del Bosque Zapopan,</div>
      <div>Jalisco 45110 - Mexico</div>
      <div class="tel">Tel (52) 33 31 55 08 72</div>
    </address>
  </section>

  <h2 class="card-label" style="top:55px;font-weight:400">BACK of Business Card</h2>
  <section class="card card-back" aria-label="Business card back">
    <div class="brand">
      <span class="brand-dot"></span>
      <span class="brand-name">Tomás Ibarrola</span>
      <span class="brand-role">Architect</span>
    </div>
  </section>

  <h2 class="card-label" style="top:318px;font-weight:400">FRONT of Business Card</h2>
  <section class="card card-front" aria-label="Business card front">
    <div class="brand">
      <span class="brand-dot"></span>
      <span class="brand-name">Tomás Ibarrola</span>
      <span class="brand-role">Architect</span>
    </div>
    <div class="card-divider"></div>
    <address class="card-contact" style="font-style:normal">
      <div>Arq. Tomás Ibarrola</div>
      <div>Calle de los Fresnos #1540</div>
      <div>Colinas del Bosque Zapopan,</div>
      <div>Jalisco 45110 - Mexico</div>
      <div class="tel">Tel (52) 33 31 55 08 72</div>
    </address>
  </section>

  <div class="brand brand-primary" aria-label="Primary logo lockup">
    <span class="brand-dot"></span>
    <span class="brand-name">Tomás Ibarrola</span>
    <span class="brand-role">Architect</span>
  </div>

</main>
</body>
</html>
```